I need a business logo and business card design for a new company in Falls Church, Virginia called 'Brightwell Clinic'. Brightwell Clinic is a primary care and walk-in clinic. The logo should have the letters 'BW' connected together. The letter 'F' should be navy blue and the letter 'C' should be orange. I have attached a several business cards and the logo should be simple and memorable. I like the Harrowgate Clinic font for my card. The card should have the simplicity of Harrowgate Clinic.

The logo should be on the upper left and the name 'Brightwell Clinic' should be next to the logo.

My name Dr. Tomas Lindqvist should be in the center of the card aligned left.
Dr. Tomas Lindqvist
Board Certified in Internal Medicine
Medical Director

The bottom left should have my address.
2917 Maple Hollow Court
Suite C
Falls Church, Virginia 22981

The bottom right should have my phone number and fax number.
Ph 555-014-2736
Fax 555-014-8490

The back of the card should have serve as an appointment reminder.
Appointment
For ____________________________________________
On _______________________at ___________________AM / PM
With ___________________________________________

If you are unable to keep your appointment, please give us 24 hour notice at 555-014-2736. Thank you.

```html
<!DOCTYPE html>
<html lang="en">
<head>
<meta charset="utf-8">
<title>Brightwell Clinic – Business Card</title>
<link rel="stylesheet" href="https://fonts.googleapis.com/css2?family=Source+Sans+3:ital,wght@0,400;0,600;0,700;1,400;1,700&display=swap">
<style>
  :root {
    --navy: #100c3a;
    --orange: #e06a0e;
    --paper: #f9f8f6;
    --cream: #f6e5d8;
    --cream-light: #f9ece2;
    --rule: #3a3550;
    --stage: #3c3c3c;
  }
  * { margin: 0; padding: 0; box-sizing: border-box; }
  html, body { width: 1200px; height: 750px; overflow: hidden; }
  body {
    background: var(--stage);
    font-family: "Source Sans 3", sans-serif;
    position: relative;
  }
  .card {
    position: absolute;
    top: 228px;
    width: 461px;
    height: 262px;
    overflow: hidden;
  }
  /* Front */
  .card-front { left: 124px; background: var(--paper); }
  .brand { position: absolute; left: 160px; top: 42px; display: flex; align-items: center; gap: 12px; }
  .brand-square { width: 46px; height: 50px; background: var(--navy); }
  .brand-name { color: var(--navy); font-weight: 400; font-size: 27px; line-height: 26px; }
  .doctor { position: absolute; left: 0; width: 100%; top: 118px; text-align: center; }
  .doctor-name { color: var(--navy); font-weight: 600; font-size: 17.5px; line-height: 22px; }
  .doctor-title { color: var(--orange); font-size: 12.5px; line-height: 17px; }
  .contact-band {
    position: absolute; left: 0; top: 172px; width: 302px; height: 90px;
    background: var(--navy); color: #fff; font-size: 11px; padding: 12px 0 0 22px;
  }
  .contact-line { display: flex; align-items: center; gap: 6px; height: 17.5px; }
  .contact-line svg { width: 12px; height: 12px; flex: none; }
  .address { margin-top: 2px; line-height: 17px; }
  .accent-block { position: absolute; left: 302px; top: 174px; width: 159px; height: 88px; background: var(--orange); }
  /* Back */
  .card-back { left: 618px; background: linear-gradient(135deg, var(--cream-light), var(--cream)); color: var(--navy); }
  .appt-title { position: absolute; left: 30px; top: 22px; font-weight: 700; font-size: 22px; }
  .back-brand { position: absolute; right: 33px; top: 28px; text-align: right; font-size: 12px; line-height: 13px; font-weight: 400; }
  .field { position: absolute; display: flex; align-items: flex-end; font-size: 13px; color: var(--navy); }
  .field .blank { border-bottom: 1px solid var(--rule); height: 1px; margin-bottom: 3px; }
  .ampm { font-size: 9.5px; margin-left: 3px; margin-bottom: 1px; }
  .notice {
    position: absolute; left: 0; width: 100%; top: 200px; text-align: center;
    font-style: italic; font-size: 14.5px; line-height: 18.5px; color: var(--navy);
  }
  .notice strong { font-weight: 700; }
</style>
</head>
<body>
  <section class="card card-front">
    <div class="brand">
      <div class="brand-square"></div>
      <div class="brand-name">Brightwell<br>Clinic</div>
    </div>
    <div class="doctor">
      <p class="doctor-name">Dr. Tomas Lindqvist</p>
      <p class="doctor-title">Board Certified in Internal Medicine | Medical Director</p>
    </div>
    <div class="contact-band">
      <div class="contact-line">
        <svg viewBox="0 0 24 24" aria-hidden="true"><path fill="#e06a0e" d="M6.6 10.8a15.1 15.1 0 0 0 6.6 6.6l2.2-2.2c.3-.3.7-.4 1-.2 1.1.4 2.3.6 3.6.6.6 0 1 .4 1 1V20c0 .6-.4 1-1 1A17 17 0 0 1 3 4c0-.6.4-1 1-1h3.5c.6 0 1 .4 1 1 0 1.3.2 2.5.6 3.6.1.3 0 .7-.2 1z"/></svg>
        <span>555-014-2736</span>
      </div>
      <div class="contact-line">
        <svg viewBox="0 0 24 24" aria-hidden="true"><path fill="#e06a0e" d="M6 3h10v5H6zM3 9h18v9H3zM6 15h12v6H6z"/></svg>
        <span>555-014-8490</span>
      </div>
      <p class="address">2917 Maple Hollow Court, Suite C<br>Falls Church, Virginia 22981</p>
    </div>
    <div class="accent-block"></div>
  </section>

  <section class="card card-back">
    <h1 class="appt-title">Appointment</h1>
    <div class="back-brand">Brightwell<br>Clinic</div>
    <div class="field" style="left:30px; top:76px;">
      <span>For</span><span class="blank" style="width:376px;"></span>
    </div>
    <div class="field" style="left:29px; top:116px;">
      <span>On</span><span class="blank" style="width:191px; margin-left:4px;"></span>
      <span style="margin-left:3px;">At</span><span class="blank" style="width:131px;"></span>
      <span class="ampm">AM/PM</span>
    </div>
    <div class="field" style="left:30px; top:159px;">
      <span>With</span><span class="blank" style="width:366px; margin-left:2px;"></span>
    </div>
    <p class="notice">If you are unable to keep your appointment, please give<br>us 24 hour notice at <strong>555-014-2736</strong>. Thank you.</p>
  </section>
</body>
</html>
```